Professional & Modern Technology Business Card

We need a business card for our software/technology firm. Our services include Program/Project Management, Project Controls and Enterprise Analytics. Our clients are usually in the Aviation, Public Works, Transportation and Electric & Water Utility industries. We serve both public and private clients. Would like a very professional, conservative but somewhat modern design. Design, Develop, Deploy is the corporate tagline. We have two offices. The headquarters is in Atlanta, GA and a satellite office In Savannah, GA. Corporate Logo Attached.
Looking to do website and corporate brochure after the successful completion of this project. Would like to begin a working relationship with best designers.
Tagline: Design, Develop, Deploy
Website: www.quambelsystems.example
My Name: Delia Marchetti
My Title: CEO
Email: dmarchetti@quambelsystems.example
Atlanta Address:
87 Corliss Avenue, #2260
Atlanta, GA 30301
Office: 404.555.0178
Fax: 404.555.0143
Mobile: 404.555.0116
Marrowfield Address:
315 West Harrow Lane Street
Suite 720
Marrowfield, SC 29998
Office: 912.555.0162
Fax: 404.555.0143
Mobile: 404.555.0116
Please include the email address in your designs: dmarchetti@quambelsystems.example.
I appreciate everyone's design efforts. Just a few notes:
1. Please remove the mobile number from the cards
2. The backs of the cards can be utilized for writing notes. Make sure your design on the back of the card is conducive to clearly adding writing if needed.
3. No black backgrounds please
4. Only use the corporate logo on the front of the card. You can use portions of the logo design, but not the logo in totality.
Thank You
Conservative

```html
<!DOCTYPE html>
<html lang="en">
<head>
<meta charset="utf-8">
<title>Quambel Systems – Business Card</title>
<link rel="stylesheet" href="https://fonts.googleapis.com/css2?family=Open+Sans:ital,wght@0,400;0,600;0,700;1,400&display=swap">
<style>
  :root {
    --teal: #175f73;
    --blue: #3263b5;
    --green: #6cc02d;
    --yellow: #e6cf06;
    --paper: #eeeeea;
    --ink: #1c1c1c;
    --fold: #0d3a46;
    --backdrop: #dcdcd8;
  }
  * { box-sizing: border-box; margin: 0; padding: 0; }
  html, body { width: 1200px; height: 1000px; overflow: hidden; }
  body {
    background: var(--backdrop);
    font-family: "Open Sans", Arial, sans-serif;
    color: var(--ink);
    position: relative;
  }
  .card {
    position: absolute;
    left: 250px;
    width: 700px;
    height: 400px;
    background: var(--paper);
    overflow: hidden;
    box-shadow: 0 6px 18px rgba(0,0,0,.18);
  }
  .card--front { top: 70px; }
  .card--back { top: 530px; }

  /* Front: stacked bands on the left */
  .bands { position: absolute; left: 0; top: 0; width: 400px; height: 400px; background: var(--teal); }
  .band { position: absolute; left: 0; width: 372px; display: flex; flex-direction: column; justify-content: center; padding-left: 40px; }
  .band--name { top: 62px; height: 92px; background: var(--blue); }
  .band--online { top: 162px; height: 92px; background: var(--green); }
  .band--phone { top: 262px; height: 80px; background: var(--yellow); }
  .fold {
    position: absolute; right: -28px; top: 0; width: 0; height: 0;
    border-left: 28px solid var(--fold);
    border-bottom: 14px solid transparent;
  }

  .person-name { font-size: 27px; font-weight: 700; letter-spacing: .3px; }
  .person-title { font-size: 12px; font-style: italic; margin-top: 2px; }
  .contact-line { display: flex; align-items: center; gap: 10px; font-size: 15px; color: #fff; line-height: 1.7; }
  .contact-line svg { width: 18px; height: 18px; flex: none; }
  .phone-line { font-size: 17px; line-height: 1.45; }
  .phone-line b { font-weight: 700; }

  /* Front: white info side */
  .info { position: absolute; left: 430px; top: 60px; width: 250px; }
  .brand { display: flex; align-items: center; gap: 12px; }
  .brand-mark { width: 44px; height: 44px; border-radius: 50%; background: var(--yellow); flex: none; }
  .brand-name { font-size: 21px; font-weight: 600; line-height: 1.15; color: var(--ink); }
  .tagline { font-size: 15px; margin-top: 18px; letter-spacing: 1px; }
  .address { display: flex; gap: 10px; margin-top: 34px; font-size: 15px; line-height: 1.4; }
  .address svg { width: 16px; height: 20px; flex: none; margin-top: 2px; }
  .address b { font-weight: 700; }

  /* Back */
  .back-brand { position: absolute; left: 44px; top: 40px; }
  .note-lines { position: absolute; left: 44px; top: 170px; width: 380px; }
  .note-line { height: 3px; margin-bottom: 62px; }
  .note-line--blue { background: var(--blue); }
  .note-line--green { background: var(--green); }
  .note-line--yellow { background: var(--yellow); }
  .back-bands { position: absolute; right: 0; top: 0; width: 230px; height: 400px; display: flex; flex-direction: column; }
  .back-band { width: 100%; }
  .back-band--teal { background: var(--teal); height: 56px; }
  .back-band--blue { background: var(--blue); height: 80px; }
  .back-band--gap { background: var(--teal); height: 10px; }
  .back-band--green { background: var(--green); height: 88px; }
  .back-band--yellow { background: var(--yellow); height: 96px; }
  .back-band--teal-end { background: var(--teal); flex: 1; }
</style>
</head>
<body>

<section class="card card--front" aria-label="Business card front">
  <div class="bands">
    <div class="band band--name">
      <span class="fold"></span>
      <p class="person-name">Delia Marchetti</p>
      <p class="person-title">Chief Executive Officer</p>
    </div>
    <div class="band band--online">
      <span class="fold"></span>
      <p class="contact-line">
        <svg viewBox="0 0 18 18"><rect x="1" y="3" width="16" height="12" fill="none" stroke="#fff" stroke-width="1.6"/><path d="M1 3l8 7 8-7M1 15l6-6M17 15l-6-6" fill="none" stroke="#fff" stroke-width="1.4"/></svg>
        dmarchetti@quambelsystems.example
      </p>
      <p class="contact-line">
        <svg viewBox="0 0 18 18"><circle cx="9" cy="9" r="7.5" fill="none" stroke="#fff" stroke-width="1.4"/><ellipse cx="9" cy="9" rx="3.2" ry="7.5" fill="none" stroke="#fff" stroke-width="1.2"/><path d="M1.5 9h15M3 5h12M3 13h12" stroke="#fff" stroke-width="1.2"/></svg>
        www.quambelsystems.example
      </p>
    </div>
    <div class="band band--phone">
      <span class="fold"></span>
      <p class="phone-line"><b>Office:</b> 912.555.0162</p>
      <p class="phone-line"><b>Fax:</b> 404.555.0143</p>
    </div>
  </div>

  <div class="info">
    <div class="brand">
      <span class="brand-mark"></span>
      <span class="brand-name">Quambel Systems, Inc.</span>
    </div>
    <p class="tagline">Design . Develop . Deploy</p>
    <div class="address">
      <svg viewBox="0 0 16 20"><path d="M8 1a6 6 0 0 0-6 6c0 4.5 6 12 6 12s6-7.5 6-12a6 6 0 0 0-6-6z" fill="none" stroke="#1c1c1c" stroke-width="1.6"/><circle cx="8" cy="7" r="2" fill="#1c1c1c"/></svg>
      <p><b>Marrowfield Address:</b><br>315 West Harrow Lane<br>Street Suite 720<br>Marrowfield, SC 29998</p>
    </div>
  </div>
</section>

<section class="card card--back" aria-label="Business card back">
  <div class="back-brand brand">
    <span class="brand-mark"></span>
    <span class="brand-name">Quambel Systems, Inc.</span>
  </div>
  <div class="note-lines">
    <div class="note-line note-line--blue"></div>
    <div class="note-line note-line--green"></div>
    <div class="note-line note-line--yellow"></div>
  </div>
  <div class="back-bands">
    <div class="back-band back-band--teal"></div>
    <div class="back-band back-band--blue"></div>
    <div class="back-band back-band--gap"></div>
    <div class="back-band back-band--green"></div>
    <div class="back-band back-band--gap"></div>
    <div class="back-band back-band--yellow"></div>
    <div class="back-band back-band--teal-end"></div>
  </div>
</section>

</body>
</html>
```